Business Card Design

A business card design must match as a cleaning company.
We do house cleaning, office, cafe , function center , club and so on.

Industry/Entity Type

House

Contact Information for Business Card

Bright Lane cleaning services
Mara Delvin
Director
0428395146
1300 917 254
Brightlane.cleaning@bluvex.com

```html
<!DOCTYPE html>
<html lang="en">
<head>
<meta charset="utf-8">
<title>Bright Lane Cleaning Services – Business Card</title>
<link href="https://fonts.googleapis.com/css2?family=Arimo:wght@400;700&display=swap" rel="stylesheet">
<style>
  :root {
    --backdrop: #c1c1c1;
    --card: #ffffff;
    --ink: #1f2221;
    --ink-soft: #2a2c2c;
    --teal-light: #3ab2cf;
    --teal: #00a8c6;
    --teal-deep: #007e86;
    --leaf: #8fbb4c;
  }
  * { box-sizing: border-box; margin: 0; padding: 0; }
  html, body {
    width: 1200px;
    height: 1000px;
    overflow: hidden;
    background: var(--backdrop);
    font-family: "Arimo", Arial, sans-serif;
  }
  .card {
    position: absolute;
    left: 170px;
    top: 234px;
    width: 860px;
    height: 531px;
    background: var(--card);
  }
  .brand {
    position: absolute;
    left: 0;
    right: 0;
    top: 168px;
    display: flex;
    align-items: center;
    justify-content: center;
    gap: 18px;
  }
  .brand-mark {
    width: 38px;
    height: 38px;
    background: var(--teal);
  }
  .brand-name {
    font-size: 32px;
    font-weight: 400;
    color: var(--ink);
    letter-spacing: 0.5px;
    white-space: nowrap;
  }
  .accent-band {
    position: absolute;
    left: 0;
    top: 357px;
    width: 418px;
    height: 123px;
    background: linear-gradient(90deg,
      var(--teal-light) 0%,
      var(--teal) 12%,
      #0097b3 55%,
      var(--teal-deep) 100%);
  }
  .contact {
    position: absolute;
    left: 446px;
    top: 372px;
    color: var(--ink-soft);
  }
  .contact-name {
    font-size: 21px;
    line-height: 28px;
    margin-left: 4px;
  }
  .contact-name strong { font-weight: 700; color: var(--ink); }
  .contact-row {
    display: flex;
    align-items: center;
    font-size: 20px;
    line-height: 28px;
    margin-top: 6px;
  }
  .contact-row + .contact-row { margin-top: 0; }
  .contact-icon {
    width: 26px;
    height: 22px;
    margin-right: 9px;
    flex: none;
  }
</style>
</head>
<body>
  <div class="card">
    <div class="brand">
      <span class="brand-mark" aria-hidden="true"></span>
      <span class="brand-name">Bright Lane Cleaning Services</span>
    </div>

    <div class="accent-band"></div>

    <div class="contact">
      <p class="contact-name"><strong>Mara Delvin</strong> ( Director )</p>
      <p class="contact-row">
        <svg class="contact-icon" viewBox="0 0 26 22" aria-hidden="true">
          <rect x="7" y="1" width="12" height="20" rx="2" fill="var(--leaf)"/>
          <rect x="9" y="3.5" width="8" height="12" fill="#fff"/>
          <circle cx="13" cy="18" r="1.3" fill="#fff"/>
        </svg>
        0428395146 , 1300 917 254
      </p>
      <p class="contact-row">
        <svg class="contact-icon" viewBox="0 0 26 22" aria-hidden="true">
          <rect x="0" y="3" width="25" height="17" rx="1.5" fill="var(--leaf)"/>
          <path d="M1 4.5 L12.5 13 L24 4.5" fill="none" stroke="#fff" stroke-width="1.6"/>
        </svg>
        Brightlane.cleaning@bluvex.com
      </p>
    </div>
  </div>
</body>
</html>
```